Author/ Speaker Business Card design

I need a business card designed that will go with the branding that is already on my book and website. I like clean and straightforward, but I am not opposed to something more 'innovative'.

Target Market(s)

Colleges and Universities, educational institutions

Industry/Entity Type

Education

Contact Information for Business Card

Standard size. It should be able to be printed on good quality white or ivory paper.

Font styles to use
Sans Serif

Colors
0355a3

Requirements
Must have
• There's a blue on my website. It should have some blue. My logo is at the top. It should have the logo incorporated somewhere on it. My name, Author | Speaker | Teacher | Trainer, my phone number (+31 64-207 5819), my email address (milo@theboldlearner.example), Social media icons (twitter, Instagram, LinkedIn) with the addresses (twitter @writermilofenwick, Instagram - theboldlearner, LinkedIn - theboldlearner) By they way, the website is www.theboldlearner.example. There is a photo of the book on the website. Also, my full name is Milo Fenwick
Nice to have
• Try to use the font that is on the website and book. Also, if you could get that blue, that would be great.
Should not have
• My photo

```html
<!DOCTYPE html>
<html lang="en">
<head>
<meta charset="utf-8">
<title>The Bold Learner – Business Card</title>
<link rel="stylesheet" href="https://fonts.googleapis.com/css2?family=Roboto:wght@300;400;500;700&display=swap">
<style>
  :root {
    --brand-blue: #0355a3;
    --paper: #ffffff;
    --backdrop: #1f1f21;
    --ink-grey: #5f6368;
  }
  * { box-sizing: border-box; margin: 0; padding: 0; }
  html, body {
    width: 1200px; height: 900px; overflow: hidden;
    background: var(--backdrop);
    font-family: "Roboto", Arial, sans-serif;
  }
  .canvas {
    width: 1200px; height: 900px;
    display: flex; flex-direction: column; align-items: center; justify-content: center;
    gap: 36px;
  }
  .card {
    width: 700px; height: 400px; position: relative;
  }
  .card-front {
    background: var(--brand-blue); color: var(--paper);
    display: flex; flex-direction: column; align-items: center; justify-content: center;
  }
  .front-brand {
    display: flex; align-items: center; gap: 18px;
    font-weight: 700; font-size: 56px; letter-spacing: -0.5px;
    margin-top: -20px;
  }
  .brand-dot {
    width: 30px; height: 30px; border-radius: 50%; background: currentColor;
  }
  .front-url {
    position: absolute; bottom: 52px; left: 0; right: 0; text-align: center;
    font-size: 19px; font-weight: 400; letter-spacing: 0.3px;
  }
  .front-url strong { font-weight: 700; }

  .card-back {
    background: var(--paper);
    display: flex; align-items: center;
  }
  .back-brand {
    width: 330px; display: flex; align-items: center; justify-content: center; gap: 12px;
    color: var(--brand-blue); font-weight: 700; font-size: 36px; letter-spacing: -0.3px;
  }
  .back-brand .brand-dot { width: 20px; height: 20px; }
  .divider {
    width: 3px; height: 196px; background: var(--brand-blue);
  }
  .contact {
    padding-left: 26px; color: var(--ink-grey);
  }
  .contact-name {
    color: var(--brand-blue); font-weight: 500; font-size: 33px;
    text-transform: uppercase; letter-spacing: 0.8px; line-height: 1;
  }
  .contact-roles {
    font-size: 17px; font-weight: 300; margin: 4px 0 12px;
  }
  .contact-list { list-style: none; font-size: 18px; font-weight: 300; line-height: 22px; }
  .contact-list li { display: flex; align-items: center; gap: 10px; }
  .contact-list .group-gap { margin-top: 10px; }
  .social-mark {
    width: 11px; height: 11px; border-radius: 50%; background: var(--brand-blue); flex: none;
  }
  .contact-list svg { width: 13px; height: 13px; flex: none; }
  .contact-list .url strong { color: var(--brand-blue); font-weight: 500; }
</style>
</head>
<body>
<main class="canvas">
  <section class="card card-front">
    <div class="front-brand"><span class="brand-dot"></span>The Bold Learner</div>
    <p class="front-url">www.<strong>theboldlearner</strong>.example</p>
  </section>

  <section class="card card-back">
    <div class="back-brand"><span class="brand-dot"></span>The Bold Learner</div>
    <div class="divider"></div>
    <div class="contact">
      <h1 class="contact-name">Milo Fenwick</h1>
      <p class="contact-roles">Author | Speaker | Teacher | Trainer</p>
      <ul class="contact-list">
        <li><span class="social-mark"></span>@writermilofenwick</li>
        <li><span class="social-mark"></span>theboldlearner</li>
        <li><span class="social-mark"></span>theboldlearner</li>
        <li class="group-gap">
          <svg viewBox="0 0 16 16" aria-hidden="true"><path d="M4 1.5l2.3 3-1.4 1.6c.8 1.9 2.2 3.4 4.1 4.2l1.6-1.4 3 2.3-1.3 2.6C7 13.5 2.5 9 1.5 2.8z" fill="var(--brand-blue)"/></svg>
          (+31 64-207 5819)
        </li>
        <li>
          <svg viewBox="0 0 16 16" aria-hidden="true"><rect x="1.5" y="3.5" width="13" height="9" fill="none" stroke="var(--brand-blue)" stroke-width="1.4"/><path d="M1.5 3.5l6.5 5 6.5-5" fill="none" stroke="var(--brand-blue)" stroke-width="1.4"/></svg>
          milo@theboldlearner.example
        </li>
        <li class="url">
          <svg viewBox="0 0 16 16" aria-hidden="true"><circle cx="8" cy="8" r="6.5" fill="none" stroke="var(--brand-blue)" stroke-width="1.3"/><ellipse cx="8" cy="8" rx="2.8" ry="6.5" fill="none" stroke="var(--brand-blue)" stroke-width="1.1"/><path d="M1.5 8h13" stroke="var(--brand-blue)" stroke-width="1.1"/></svg>
          <span>www.<strong>theboldlearner</strong>.example</span>
        </li>
      </ul>
    </div>
  </section>
</main>
</body>
</html>
```